Tallyleaf Web Design

Create Website Design for Tallyleaf. Tallyleaf is online application for collaboration team work system (task list management). More concept design for this project please find attach file ("tallyleaf website concept.pdf") . But my concept is just describe minimal features not bind design

For tallyleaf logo, i had already attach files. But i had not decided what color i chose, so it's okay if you suggest logo color for your suitable website design.
Updates

Dear All Designer,

I like brisk carousel (http://quorvanlabs.example/brisk-carousel/),
may be your concept design can adjust with this concept.
but don't worry about script for brisk carousel, my team will be handle
You just make website design to suitable with brisk carousel

but if you had own website design concept are welcome

thanks

Target Market(s)

Business Company

Industry/Entity Type

Management

```html
<!DOCTYPE html>
<html lang="en">
<head>
<meta charset="utf-8">
<title>Tallyleaf – Collaboration Application</title>
<link href="https://fonts.googleapis.com/css2?family=Fira+Sans:wght@400;500;600&display=swap" rel="stylesheet">
<style>
:root{
  --cream:#fdf8dc;
  --lime:#a6d53c;
  --teal:#1ab3c5;
  --teal-dark:#1592a3;
  --navy:#2d3a8c;
  --nav-text:#1a8ba0;
  --heading:#555;
  --body:#444;
  --footer-line:#3cc4ad;
  --white:#fff;
}
*{margin:0;padding:0;box-sizing:border-box}
html,body{width:1200px;height:644px;overflow:hidden}
body{position:relative;background:var(--white);font-family:"Fira Sans",sans-serif}
.site-header{position:absolute;left:0;top:0;width:1200px;height:60px;background:var(--cream);border-bottom:3px solid var(--lime);height:63px}
.brand{position:absolute;left:312px;top:10px;display:flex;align-items:center;gap:6px;color:#1aa9b8;font-weight:600;font-size:34px;letter-spacing:-.5px;line-height:1}
.brand-dot{width:14px;height:14px;border-radius:50%;background:var(--navy)}
.login-tab{position:absolute;left:462px;top:-24px;width:48px;height:37px;border-radius:0 0 24px 24px;background:var(--lime);color:var(--white);font-size:8px;text-align:center;padding-top:25px;text-decoration:none}
.main-nav{position:absolute;left:589px;top:31px;display:flex;align-items:center}
.nav-home{width:37px;height:37px;border:3px solid var(--lime);border-radius:50%;display:flex;align-items:center;justify-content:center;background:var(--cream);margin-right:19px}
.main-nav a.nav-link{color:var(--nav-text);font-size:9px;font-weight:500;text-decoration:none;margin-right:22px}
.hero{position:absolute;left:312px;top:84px;width:575px;height:221px;background:linear-gradient(100deg,#dfedb2 0%,#eef5cf 45%,#fbfbe8 100%)}
.hero-caption{position:absolute;left:570px;top:141px;width:317px;height:107px;background:var(--teal);border-bottom:4px solid var(--navy);border-radius:6px 6px 4px 4px;color:var(--white);padding:20px 14px}
.hero-caption h1{font-size:27px;font-weight:500;line-height:1.1}
.hero-caption p{font-size:17px;font-weight:500;margin-top:9px}
.feature{position:absolute;top:340px;width:170px;text-align:center}
.feature h2{font-size:11.5px;font-weight:500;color:var(--heading);height:22px}
.feature-icon{display:block;margin:8px auto 0}
.feature p{font-size:8.6px;line-height:1.3;color:var(--body);margin-top:8px}
.site-footer{position:absolute;left:0;top:511px;width:1200px;height:133px;background:var(--teal)}
.footer-nav{position:absolute;left:311px;top:24px;display:flex;gap:19px}
.footer-nav a{color:var(--white);font-size:9px;text-decoration:none}
.social{position:absolute;left:780px;top:20px;display:flex;gap:20px}
.social span{width:21px;height:19px;background:var(--white);border-radius:4px}
.social span.round{border-radius:50%;width:22px}
.footer-rule{position:absolute;left:0;top:76px;width:1200px;height:3px;background:var(--footer-line)}
.footer-brand{position:absolute;left:0;top:91px;width:1200px;text-align:center;color:var(--white);font-size:28px;font-weight:600;letter-spacing:-.5px}
</style>
</head>
<body>
<header class="site-header">
  <div class="brand"><span>tallyleaf</span><span class="brand-dot"></span></div>
  <a class="login-tab" href="#">Login</a>
  <nav class="main-nav">
    <a class="nav-home" href="#" aria-label="Home">
      <svg width="15" height="14" viewBox="0 0 15 14"><path d="M1.5 7 7.5 1.5 13.5 7M3.5 5.5V12.5H11.5V5.5" fill="none" stroke="#2d3a8c" stroke-width="2" stroke-linejoin="round"/></svg>
    </a>
    <a class="nav-link" href="#">Services</a>
    <a class="nav-link" href="#">Support</a>
    <a class="nav-link" href="#">Pricing</a>
    <a class="nav-link" href="#">Free Trial</a>
    <a class="nav-link" href="#">Contact</a>
  </nav>
</header>

<div class="hero" role="img" aria-label="Sketched illustration of team members surrounded by laptops, phones, cloud and calendar doodles"></div>
<div class="hero-caption">
  <h1>Customize</h1>
  <p>application online collaboration system</p>
</div>

<section class="feature" style="left:310px">
  <h2>Customize Application</h2>
  <svg class="feature-icon" width="66" height="66" viewBox="0 0 66 66"><circle cx="33" cy="33" r="30" fill="#fff" stroke="#a6d53c" stroke-width="4"/><path d="M20 36V27h24m-5-5 5 5-5 5M46 30v9H22m5 5-5-5 5-5" fill="none" stroke="#2d3a8c" stroke-width="2.5" stroke-linecap="round" stroke-linejoin="round"/></svg>
  <p>Jujubes jelly beans pastry cake biscuit jujubes oat cake. Candy canes candy canes topping lemon drops liquorice.</p>
</section>
<section class="feature" style="left:516px">
  <h2>Synchronize All Device</h2>
  <svg class="feature-icon" width="66" height="66" viewBox="0 0 66 66"><circle cx="33" cy="33" r="30" fill="#fff" stroke="#a6d53c" stroke-width="4"/><path d="M19 41a7 7 0 0 1 0-14 9 9 0 0 1 16-4 8 8 0 0 1 11 5 7 7 0 0 1 0 13z" fill="none" stroke="#2d3a8c" stroke-width="3" stroke-linejoin="round"/></svg>
  <p>Jujubes jelly beans pastry cake biscuit jujubes oat cake. Candy canes candy canes topping lemon drops liquorice.</p>
</section>
<section class="feature" style="left:720px">
  <h2>Report</h2>
  <svg class="feature-icon" width="66" height="66" viewBox="0 0 66 66"><circle cx="33" cy="33" r="30" fill="#fff" stroke="#a6d53c" stroke-width="4"/><path d="M25 20h17l-2 24H21z" fill="#2d3a8c"/><path d="M27 25h11M26 30h11M25 35h11" stroke="#fff" stroke-width="1.6"/><path d="M19 28h4M18 33h4" stroke="#2d3a8c" stroke-width="1.6"/></svg>
  <p>Jujubes jelly beans pastry cake biscuit jujubes oat cake. Candy canes candy canes topping lemon drops liquorice.</p>
</section>

<footer class="site-footer">
  <nav class="footer-nav">
    <a href="#">Home</a><a href="#">Servises</a><a href="#">Support</a><a href="#">Pricing</a><a href="#">Free Trial</a><a href="#">Contact</a>
  </nav>
  <div class="social" aria-label="Social links"><span></span><span class="round"></span><span></span></div>
  <div class="footer-rule"></div>
  <div class="footer-brand">tallyleaf</div>
</footer>
</body>
</html>
```